Banner Design 4040mm W x 2190mm H

Design a glamorous and exciting 4040mm W x 2190mm H backdrop for the QRTLB Silver Orchid Gala at the luxurious Maple Hall, Vesta, Wintermoor, Sydney. This exciting backdrop should be spectacular so that people will be excited to take photos in front of it.
Design Colours preferred is black and pink.
Please include our website on the banner www.qrtlb.org.au
Should include the words "QRTLB Silver Orchid Gala" as the main attraction on the banner.
Please include "Thank you to our sponsors" and include the logo of the sponsors.
Sponsors:
Hollins Pathology
Brightvale Radiology
KMT Diagnostic Imaging
Oakfield Legal Group
Tandrels
Banner Template:
4040mm W x 2190mm H Single Sided (.AI)
https://files.examplestore.net/d/8ZkQ2mTr7LwX4pNvB9cY1hJ5sFgD3aE6/view
QRTLB Logo:
Can be obtained from our website www.qrtlb.org.au

```html
<!DOCTYPE html>
<html lang="en">
<head>
<meta charset="utf-8">
<title>QRTLB Silver Orchid Gala – Sponsor Backdrop</title>
<link rel="stylesheet" href="https://fonts.googleapis.com/css2?family=Marcellus&family=Poppins:wght@400;600;700&display=swap">
<style>
  :root {
    --page-bg: #f1f1f1;
    --deep-purple: #3a1f74;
    --violet: #5e2386;
    --magenta: #a22a86;
    --hot-pink: #c2368f;
    --ember: #c8402c;
    --sunset-orange: #e8702a;
    --glow-gold: #ffc24a;
    --charcoal: #2b2a2b;
    --white: #ffffff;
    --sponsor-red: #e4234f;
    --sponsor-navy: #1d3f8f;
    --sponsor-purple: #6b4ea0;
    --sponsor-gold: #c9a43a;
  }
  * { box-sizing: border-box; margin: 0; padding: 0; }
  html, body {
    width: 959px; height: 1200px; overflow: hidden;
    background: var(--page-bg);
  }
  .backdrop {
    position: absolute; left: 30px; top: 356px;
    width: 899px; height: 488px;
    overflow: hidden;
    box-shadow: 0 8px 18px rgba(0,0,0,0.25);
    font-family: "Poppins", sans-serif;
  }
  .hero-photo {
    position: absolute; left: 0; top: 0; width: 899px; height: 334px;
    background:
      radial-gradient(ellipse 260px 150px at 760px 90px, rgba(255,194,74,0.85) 0%, rgba(255,140,40,0.45) 45%, rgba(232,112,42,0) 75%),
      radial-gradient(ellipse 220px 110px at 560px 210px, rgba(240,90,40,0.75) 0%, rgba(200,64,44,0) 80%),
      radial-gradient(ellipse 180px 70px at 640px 300px, rgba(255,170,60,0.6) 0%, rgba(255,170,60,0) 80%),
      radial-gradient(ellipse 140px 90px at 700px 200px, rgba(140,170,230,0.55) 0%, rgba(140,170,230,0) 80%),
      linear-gradient(180deg, rgba(40,10,50,0) 70%, rgba(60,15,55,0.55) 100%),
      linear-gradient(100deg, var(--deep-purple) 0%, var(--violet) 22%, var(--magenta) 42%, var(--ember) 62%, var(--sunset-orange) 82%, #f08a2c 100%);
  }
  .event-title { position: absolute; left: 90px; top: 40px; }
  .title-row { display: flex; align-items: center; gap: 28px; }
  .client-mark {
    width: 76px; height: 76px; border-radius: 50%;
    background: var(--white);
  }
  .client-name {
    font-family: "Marcellus", serif; font-weight: 400;
    font-size: 90px; line-height: 1; color: var(--white);
  }
  .event-name {
    margin-top: 8px;
    font-family: "Poppins", sans-serif; font-weight: 700;
    font-size: 40px; line-height: 1; color: var(--white);
  }
  .sponsor-heading-bar {
    position: absolute; left: 0; top: 334px; width: 899px; height: 39px;
    background: linear-gradient(90deg, var(--charcoal) 0%, #3a2c38 30%, #8a3a78 65%, var(--hot-pink) 100%);
    display: flex; align-items: center; justify-content: space-between;
    padding: 0 29px 0 44px; color: var(--white);
  }
  .sponsor-heading { font-weight: 700; font-size: 24px; }
  .website { font-weight: 400; font-size: 19px; }
  .accent-strip {
    position: absolute; left: 0; top: 373px; width: 899px; height: 14px;
    background: linear-gradient(90deg, #2a1045 0%, #5a1f6a 50%, #c85a3a 85%, var(--sunset-orange) 100%);
  }
  .sponsor-band {
    position: absolute; left: 0; top: 387px; width: 899px; height: 76px;
    background: var(--white);
    list-style: none;
    display: grid; grid-template-columns: repeat(5, 1fr);
    align-items: center; padding: 0 30px;
  }
  .sponsor {
    display: flex; align-items: center; justify-content: center; gap: 8px;
    font-family: "Poppins", sans-serif; font-weight: 600;
    font-size: 17px; line-height: 1.1;
  }
  .sponsor-name { display: block; }
  .sponsor-mark { width: 26px; height: 26px; flex: none; }
  .sponsor-mark.circle { border-radius: 50%; }
  .sponsor--hollins { color: var(--sponsor-red); }
  .sponsor--hollins .sponsor-mark { background: var(--sponsor-navy); width: 14px; height: 20px; }
  .sponsor--brightvale { color: var(--sponsor-navy); }
  .sponsor--brightvale .sponsor-mark { border: 3px solid var(--sponsor-navy); }
  .sponsor--kmt { color: var(--sponsor-purple); }
  .sponsor--kmt .sponsor-mark { background: var(--sponsor-purple); width: 34px; height: 34px; }
  .sponsor--oakfield { color: var(--sponsor-gold); text-align: center; }
  .sponsor--tandrels { color: var(--white); }
  .tandrels-tile {
    background: var(--sponsor-navy);
    padding: 10px 12px; font-size: 17px;
  }
  .base-strip {
    position: absolute; left: 0; top: 463px; width: 899px; height: 25px;
    background: linear-gradient(90deg, #2a0f3e 0%, #4a1a5c 45%, #a8423f 80%, var(--sunset-orange) 100%);
  }
</style>
</head>
<body>
  <main class="backdrop">
    <div class="hero-photo" role="img" aria-label="Night photograph of an illuminated orange steel arch bridge over a river with a glowing city skyline under a purple and magenta sky"></div>

    <header class="event-title">
      <div class="title-row">
        <span class="client-mark" aria-hidden="true"></span>
        <h1 class="client-name">QRTLB</h1>
      </div>
      <p class="event-name">Silver Orchid Gala</p>
    </header>

    <div class="sponsor-heading-bar">
      <h2 class="sponsor-heading">Thank&nbsp; You to Our Sponsors</h2>
      <span class="website">www.qrtlb.org.au</span>
    </div>

    <div class="accent-strip"></div>

    <ul class="sponsor-band">
      <li class="sponsor sponsor--hollins"><span class="sponsor-mark"></span><span class="sponsor-name">Hollins<br>Pathology</span></li>
      <li class="sponsor sponsor--brightvale"><span class="sponsor-mark circle"></span><span class="sponsor-name">Brightvale<br>Radiology</span></li>
      <li class="sponsor sponsor--kmt"><span class="sponsor-mark circle"></span><span class="sponsor-name">KMT Diagnostic<br>Imaging</span></li>
      <li class="sponsor sponsor--oakfield"><span class="sponsor-name">Oakfield<br>Legal Group</span></li>
      <li class="sponsor sponsor--tandrels"><span class="sponsor-name tandrels-tile">Tandrels</span></li>
    </ul>

    <div class="base-strip"></div>
  </main>
</body>
</html>
```